a business advisory consulting website

I need a website 3-5 pages to sell my professional services in IT and Project management Consulting. My company name is Tidewell Advisory Consulting. I want it to be device friendly and easy to navigate for the busy executive however intriguing enough.
I have attached some info I drafted on About the company and personal Bio. Also there is a website that I really like that I have attached the initial site pdf and websites that I like are here: https://quillmarkfunds.example, https://lumetratrends.example, https://www.corbelteachingconsulting.example as examples. Thanks
Updates

Hi Designers, I have uploaded the logo in 3D .png format, to assist in the web design.

Target Market(s)

B2B, governments, IT companies, Project Management companies and Consulting firms, small medium enterprises to large corporate enterprises.

Industry/Entity Type

It Professional

Coding

Coded - Design and coding required

Number of Pages Required

5+ page

Font styles to use
Sans Serif

Requirements
Must have
• Home, About company, the team, what we do and contact us
Nice to have
• Blog
Should not have
• pop ups, flash

```html
<!DOCTYPE html>
<html lang="en">
<head>
<meta charset="utf-8">
<title>Tidewell Advisory Consulting</title>
<link rel="stylesheet" href="https://fonts.googleapis.com/css2?family=Montserrat:wght@400;500;600;700&family=Raleway:wght@400;500&display=swap">
<style>
:root{
  --red:#e62a2c;
  --navy:#232c4f;
  --ink:#2a3350;
  --body:#7d8190;
  --soft:#eef0f6;
  --white:#ffffff;
}
*{box-sizing:border-box;margin:0;padding:0}
html,body{width:1200px;height:3618px;overflow:hidden}
body{position:relative;background:var(--white);font-family:"Raleway",sans-serif;color:var(--ink)}
.abs{position:absolute}
.site-header{position:absolute;left:0;top:0;width:1200px;height:108px;background:var(--white)}
.brand{position:absolute;left:92px;top:22px;display:flex;align-items:center;gap:10px;font-family:"Montserrat",sans-serif;font-weight:700;font-size:24px;color:var(--navy);letter-spacing:.5px;line-height:1}
.brand-mark{width:18px;height:18px;background:var(--red)}
.nav{position:absolute;top:32px;font-family:"Montserrat",sans-serif;font-size:14px;font-weight:600;color:var(--ink);letter-spacing:.3px}
.hero{position:absolute;left:0;top:77px;width:1200px;height:670px;background:linear-gradient(100deg,#9fb0bd 0%,#c7d2da 40%,#7d8e9a 100%)}
.hero-photo{position:absolute;left:0;top:0;width:1200px;height:670px;background:radial-gradient(ellipse at 78% 55%,#27303d 0%,#3b4654 28%,rgba(130,150,165,0) 55%)}
.hero-shade{position:absolute;left:0;top:0;width:1200px;height:670px}
.hero-title{position:absolute;left:112px;top:232px;font-family:"Montserrat",sans-serif;font-weight:600;font-size:49px;line-height:60px;color:var(--white);letter-spacing:.3px}
.hero-title .accent{color:var(--red)}
.slider-dots{position:absolute;left:542px;top:611px;width:90px;height:33px;background:var(--red);border-radius:17px;display:flex;justify-content:center;align-items:center;gap:11px}
.slider-dots span{width:9px;height:9px;border-radius:50%;background:var(--white)}
.eyebrow{position:absolute;width:1200px;text-align:center;font-family:"Montserrat",sans-serif;font-weight:600;font-size:22px;color:var(--red)}
.section-title{position:absolute;width:1200px;text-align:center;font-family:"Montserrat",sans-serif;font-weight:400;font-size:28px;color:var(--ink)}
.service{position:absolute;top:982px;width:330px}
.service-icon{position:absolute;left:0;top:0;width:73px;height:73px;border-radius:50%;background:var(--red);display:flex;align-items:center;justify-content:center}
.service h3{position:absolute;left:88px;top:2px;width:230px;font-family:"Montserrat",sans-serif;font-weight:600;font-size:17px;line-height:22px;color:var(--navy)}
.service p{position:absolute;left:88px;top:62px;width:232px;font-size:15.5px;line-height:20px;color:var(--body)}
.about{position:absolute;left:0;top:1242px;width:1200px;height:594px;background:var(--soft)}
.about-frame{position:absolute;left:76px;top:271px;width:207px;height:244px;border-left:14px solid var(--red);border-bottom:14px solid var(--red);border-radius:0 0 0 6px}
.about-photo{position:absolute;left:93px;top:103px;width:397px;height:395px;border-radius:6px;background:linear-gradient(160deg,#dfe4e8 0%,#b9c2c8 45%,#2c2f36 70%,#1e2126 100%)}
.about-eyebrow{position:absolute;left:618px;top:99px;font-family:"Montserrat",sans-serif;font-weight:600;font-size:22px;color:var(--red)}
.about-title{position:absolute;left:618px;top:135px;font-family:"Montserrat",sans-serif;font-weight:400;font-size:28px;line-height:34px;color:var(--ink)}
.about-text{position:absolute;left:622px;width:484px;font-size:15.5px;line-height:20px;color:var(--body);text-align:justify}
.reason{position:absolute;width:550px}
.reason svg{position:absolute;left:0;top:0}
.reason h4{position:absolute;left:93px;top:0;font-family:"Montserrat",sans-serif;font-weight:400;font-size:15.5px;color:var(--ink);white-space:nowrap}
.reason p{position:absolute;left:94px;top:23px;width:392px;font-size:15.5px;line-height:20px;color:var(--body);text-align:justify}
.testimonials{position:absolute;left:0;top:2379px;width:1200px;height:723px;background:var(--soft)}
.client{position:absolute;top:184px;width:290px}
.client-photo{position:absolute;top:0;width:250px;height:248px;border-radius:6px}
.client-frame{position:absolute;top:130px;width:131px;height:128px;border-left:9px solid var(--red);border-bottom:9px solid var(--red);border-radius:0 0 0 5px}
.client h5{position:absolute;top:298px;width:290px;text-align:center;font-family:"Montserrat",sans-serif;font-weight:600;font-size:17px;color:var(--red)}
.client .role{position:absolute;top:320px;width:290px;text-align:center;font-family:"Montserrat",sans-serif;font-weight:500;font-size:13px;color:var(--navy)}
.client p{position:absolute;top:341px;left:20px;width:250px;text-align:center;font-size:15.5px;line-height:20px;color:var(--body)}
.arrow{position:absolute;top:2874px}
.contact{position:absolute;left:0;top:3102px;width:1200px;height:467px;background:var(--red);color:var(--white)}
.contact-title{position:absolute;left:0;top:42px;width:1185px;text-align:center;font-family:"Montserrat",sans-serif;font-weight:600;font-size:22px}
.col-title{position:absolute;top:134px;font-family:"Montserrat",sans-serif;font-weight:600;font-size:17px}
.info-line{position:absolute;left:128px;font-family:"Montserrat",sans-serif;font-weight:600;font-size:13.5px;white-space:nowrap}
.info-icon{position:absolute;left:91px}
.info-strip{position:absolute;left:73px;top:140px;width:46px;height:166px;background:rgba(255,255,255,.08)}
.quick-link{position:absolute;left:549px;font-family:"Montserrat",sans-serif;font-weight:600;font-size:13.5px}
.social{position:absolute;top:370px;width:31px;height:31px;border:1.5px solid var(--white);border-radius:50%}
.field{position:absolute;left:814px;width:293px;height:31px;background:var(--white);border:1px solid #d9d9d9;font-family:Arial,sans-serif;font-size:12px;color:#b5b5b5;padding:8px 10px}
.check{position:absolute;left:814px;top:3467px;font-family:Arial,sans-serif;font-size:12.5px;color:var(--white);display:flex;align-items:center;gap:6px}
.check span{width:14px;height:14px;background:var(--white);border-radius:2px}
.send{position:absolute;left:814px;top:3495px;width:83px;height:32px;background:var(--navy);color:var(--white);font-family:"Montserrat",sans-serif;font-weight:600;font-size:13px;display:flex;align-items:center;justify-content:center}
.site-footer{position:absolute;left:0;top:3569px;width:1200px;height:49px;background:var(--navy);color:var(--white);font-family:"Montserrat",sans-serif;font-weight:500;font-size:12.5px;text-align:center;line-height:49px}
</style>
</head>
<body>

<header class="site-header">
  <div class="brand"><span class="brand-mark"></span>TIDEWELL ADVISORY</div>
  <nav>
    <span class="nav" style="left:449px">HOME</span>
    <span class="nav" style="left:526px">ABOUT</span>
    <span class="nav" style="left:606px">COMPANY</span>
    <span class="nav" style="left:712px">THE TEAM</span>
    <span class="nav" style="left:817px">BLOG</span>
    <span class="nav" style="left:888px">WHAT WE DO</span>
    <span class="nav" style="left:1012px">CONTACT US</span>
  </nav>
</header>

<section class="hero">
  <div class="hero-photo" role="img" aria-label="Confident businesswoman in a dark suit with arms crossed, standing in a bright modern office"></div>
  <svg class="hero-shade" width="1200" height="670" viewBox="0 0 1200 670">
    <polygon points="0,0 676,0 576,670 0,670" fill="#262c44" opacity=".82"/>
  </svg>
  <h1 class="hero-title"><span class="accent">GENUINE</span> CLIENT<br>PARTNERSHIP</h1>
  <div class="slider-dots"><span></span><span></span><span></span></div>
</section>

<section class="what-we-do">
  <div class="eyebrow" style="top:811px">WHAT WE DO</div>
  <h2 class="section-title" style="top:847px">GENUINE CLIENT PARTNERSHIP</h2>

  <article class="service" style="left:93px">
    <div class="service-icon">
      <svg width="36" height="36" viewBox="0 0 36 36" fill="none" stroke="#fff" stroke-width="2" stroke-linejoin="round"><path d="M4 22l8-2 8-12 4 1-4 11 8-2 3-4 2 1-2 7-7 3-10 3-4 6-3-1 2-6-6 1z"/></svg>
    </div>
    <h3>Follow a strategy that works</h3>
    <p>Across the three levels of Gov­ernment – Federal, State and Local – leaders continually face complex decisions around how to allocate limited resources.</p>
  </article>

  <article class="service" style="left:443px">
    <div class="service-icon">
      <svg width="36" height="36" viewBox="0 0 36 36" fill="none" stroke="#fff" stroke-width="2"><path d="M5 31h26M8 31V21M14 31V17M20 31V19M26 31V12M7 15l7-5 6 3 9-7"/></svg>
    </div>
    <h3>The best consulting services</h3>
    <p>Across the three levels of Gov­ernment – Federal, State and Local – leaders continually face complex decisions around how to allocate limited resources.</p>
  </article>

  <article class="service" style="left:794px">
    <div class="service-icon">
      <svg width="36" height="36" viewBox="0 0 36 36" fill="none" stroke="#fff" stroke-width="2"><rect x="8" y="4" width="20" height="28" rx="2"/><rect x="12" y="8" width="12" height="5"/><path d="M12 18h3M17 18h3M22 18h2M12 23h3M17 23h3M22 23h2M12 28h3M17 28h3M22 28h2"/></svg>
    </div>
    <h3>Top Project Management Agency</h3>
    <p>Across the three levels of Gov­ernment – Federal, State and Local – leaders continually face complex decisions around how to allocate limited resources.</p>
  </article>
</section>

<section class="about">
  <div class="about-frame"></div>
  <div class="about-photo" role="img" aria-label="Smiling businessman in a dark suit holding a tablet in a bright office"></div>
  <div class="about-eyebrow">ABOUT US</div>
  <h2 class="about-title">WE APPROACH BUSINESS<br>CONSULTING DIFFERENTLY</h2>
  <p class="about-text" style="top:232px">Across the three levels of Government – Federal, State and Local – leaders continually face complex decisions around how to allocate limited resources.Across the three levels of Government – Federal, State and Local – leaders continually face complex decisions around how to allocate limited resources.Across the three levels of Government – Federal, State and Local – leaders continually face complex decisions around how to allocate limited resources.</p>
  <p class="about-text" style="top:392px">Across the three levels of Government – Federal, State and Local – leaders continually face complex decisions around how to allocate limited resources.Across the three levels of Government – Federal, State and Local – leaders continually.</p>
</section>

<section class="why-we-exist">
  <div class="eyebrow" style="top:1880px">WHY WE EXIST</div>
  <h2 class="section-title" style="top:1916px">GENUINE CLIENT PARTNERSHIP</h2>

  <div class="reason" style="left:112px;top:2040px">
    <svg width="60" height="56" viewBox="0 0 60 56" fill="none" stroke-width="3"><circle cx="24" cy="22" r="14" stroke="#232c4f"/><path d="M34 32l14 14" stroke="#232c4f" stroke-width="5" stroke-linecap="round"/><path d="M2 22l10-6 8 10 8-12 8 6 12-6" stroke="#e62a2c" stroke-width="2"/></svg>
    <h4>MARKET ENTRY</h4>
    <p>We conduct market research and competitor analysis, develop strategy models and use our insights to help our clients rationalize and optimize operational processes more efficiently</p>
  </div>

  <div class="reason" style="left:620px;top:2040px">
    <svg width="56" height="56" viewBox="0 0 56 56"><circle cx="43" cy="27" r="16" fill="#232c4f"/><circle cx="43" cy="27" r="9" fill="#e62a2c"/><circle cx="43" cy="27" r="4" fill="#fff"/></svg>
    <h4 style="left:94px">ANALYTICS + BUSINESS-PROCESS OPTIMIZATION</h4>
    <p>We conduct market research and competitor analysis, develop strategy models and use our insights to help our clients rationalize and optimize operational processes more efficiently</p>
  </div>

  <div class="reason" style="left:112px;top:2190px">
    <svg width="60" height="60" viewBox="0 0 60 60" fill="none"><path d="M12 20a18 16 0 0 1 36 0z" fill="#232c4f"/><path d="M30 20v18" stroke="#232c4f" stroke-width="2"/><circle cx="30" cy="40" r="8" stroke="#e62a2c" stroke-width="2"/><path d="M40 34h14M40 40h14M40 46h14" stroke="#e62a2c" stroke-width="2"/></svg>
    <h4>FINANCE + ACCOUNTING + INSURANCE</h4>
    <p>We conduct market research and competitor analysis, develop strategy models and use our insights to help our clients rationalize and optimize operational processes more efficiently</p>
  </div>

  <div class="reason" style="left:620px;top:2190px">
    <svg width="60" height="60" viewBox="0 0 60 60" fill="none" stroke-width="2.5"><path d="M23 40c-10-6-10-24 4-26 8-1 14 6 12 14-1 5-5 7-5 12z" stroke="#232c4f"/><path d="M24 44h10M25 48h8" stroke="#232c4f"/><circle cx="38" cy="12" r="6" stroke="#e62a2c"/></svg>
    <h4 style="left:94px">IT &amp; PROJECT MANAGEMENT</h4>
    <p>We conduct market research and competitor analysis, develop strategy models and use our insights to help our clients rationalize and optimize operational processes more efficiently</p>
  </div>
</section>

<section class="testimonials">
  <div class="eyebrow" style="top:49px">TESTIMONIALS</div>
  <h2 class="section-title" style="top:85px">OUR CLIENTS SAY</h2>

  <article class="client" style="left:82px">
    <div class="client-frame" style="left:10px"></div>
    <div class="client-photo" role="img" aria-label="Portrait of a senior executive in a dark suit with arms crossed" style="left:20px;background:linear-gradient(170deg,#c9d0d4 0%,#9aa4ab 40%,#2b3038 75%,#20242b 100%)"></div>
    <h5>WALTER BRENNICK</h5>
    <div class="role">Chairman Orlan Shipping Co.</div>
    <p>We conduct market research and competitor analysis, develop strat­egy models and use our insights to help our clients rationalize and optimize operational processes more efficiently.</p>
  </article>

  <article class="client" style="left:453px">
    <div class="client-frame" style="left:8px"></div>
    <div class="client-photo" role="img" aria-label="Portrait of a smiling young man in a grey cardigan" style="left:20px;background:linear-gradient(170deg,#6f6a63 0%,#8a7f71 40%,#3f4a5a 75%,#5d6470 100%)"></div>
    <h5>MARCO DELANY</h5>
    <div class="role">Ceo, Veltrix Systems</div>
    <p>We conduct market research and competitor analysis, develop strat­egy models and use our insights to help our clients rationalize and optimize operational processes more efficiently.</p>
  </article>

  <article class="client" style="left:833px">
    <div class="client-photo" role="img" aria-label="Portrait of a smiling businesswoman in a dark blazer" style="left:23px;background:linear-gradient(170deg,#e1e6ea 0%,#c2ccd3 40%,#2f333b 75%,#24272d 100%)"></div>
    <h5>ELISE CARROW</h5>
    <div class="role">Ceo, Fennmoor Research</div>
    <p>We conduct market research and competitor analysis, develop strat­egy models and use our insights to help our clients rationalize and optimize operational processes more efficiently.</p>
  </article>
</section>
<svg class="arrow" style="left:58px" width="12" height="20" viewBox="0 0 12 20"><path d="M9 3L3 10l6 7" fill="none" stroke="#2a3350" stroke-width="1.5"/></svg>
<svg class="arrow" style="left:1130px" width="12" height="20" viewBox="0 0 12 20"><path d="M3 3l6 7-6 7" fill="none" stroke="#2a3350" stroke-width="1.5"/></svg>

<section class="contact">
  <h2 class="contact-title">GET IN TOUCH</h2>

  <div class="info-strip"></div>
  <div class="col-title" style="left:128px">TIDEWELL ADVISORY</div>
  <svg class="info-icon" style="top:172px" width="14" height="14" viewBox="0 0 14 14"><path d="M3 1l3 3-2 2c1 2 2 3 4 4l2-2 3 3-2 2C6 12 2 8 1 3z" fill="#fff"/></svg>
  <div class="info-line" style="top:171px">+1 555 014 2207 / +1 555 018 6631</div>
  <svg class="info-icon" style="top:208px" width="15" height="12" viewBox="0 0 15 12"><rect width="15" height="12" rx="1" fill="#fff"/><path d="M0 1l7.5 6L15 1" fill="none" stroke="#e62a2c" stroke-width="1.3"/></svg>
  <div class="info-line" style="top:206px">hello@quillmarkfunds.example</div>
  <svg class="info-icon" style="top:240px;left:93px" width="11" height="15" viewBox="0 0 11 15"><path d="M5.5 0A5.5 5.5 0 0 0 0 5.5C0 9 5.5 15 5.5 15S11 9 11 5.5A5.5 5.5 0 0 0 5.5 0z" fill="#fff"/><circle cx="5.5" cy="5.5" r="2" fill="#e62a2c"/></svg>
  <div class="info-line" style="top:241px">4th Floor, Wing C. Harbor Crest House,</div>
  <div class="info-line" style="top:276px">Linden Row, P.O. Box 40120 – 00311,</div>
  <div class="info-line" style="top:310px">Eastvale</div>

  <span class="social" style="left:128px"></span>
  <span class="social" style="left:167px"></span>
  <span class="social" style="left:206px"></span>
  <span class="social" style="left:245px"></span>

  <div class="col-title" style="left:545px">QUICK LINKS</div>
  <div class="quick-link" style="top:171px">Home</div>
  <div class="quick-link" style="top:206px">Our Team</div>
  <div class="quick-link" style="top:241px">Services</div>
  <div class="quick-link" style="top:276px">Solutions</div>
  <div class="quick-link" style="top:311px">Contact Us</div>
</section>

<form class="contact-form">
  <div class="field" style="top:3236px">Your Name</div>
  <div class="field" style="top:3274px">Organization</div>
  <div class="field" style="top:3311px">Phone</div>
  <div class="field" style="top:3348px">Email</div>
  <div class="field" style="top:3387px;height:73px">Write Us</div>
  <div class="check"><span></span>Request brochure/company profile.</div>
  <div class="send">SEND</div>
</form>

<footer class="site-footer">© 2019 Tidewell Advisory, LLC. All Rights Reserved.</footer>

</body>
</html>
```